Onboarding Infographic/brochure

We are a small criminal defense firm looking to create some sort of infographic or brochure that we can onboard new clients with. We are currently sending it out via email but want something a bit cooler and fun to send to clients. The information is:

A Few Quick Rules

We are here to help each step of the way. While questions are never discouraged, this letter will answer some of the most common ones we get asked.

Communications

As a client, you should always be in the loop. While we will try to respond to questions as quickly as possible, sometimes we are unable to respond right away. Do not worry - we promise to get back to you soon. Some questions might take some time to research, and a correct answer is better than a quick one.

Appointments

One of the benefits of having an attorney is the ability to discuss your case outside of court, minus the stress and headaches. If you need an appointment, please contact the office.

Appointments must be scheduled in advance. We do not want you to make a special trip to the office only to learn that we are in court or otherwise unavailable.

Jail Visits

If your family member is currently in jail, we take that very seriously. We will visit your loved one and introduce ourselves. While the case is ongoing, we ask that a family member be designated a “contact” person so that messages can be relayed quickly. Never discuss the facts of the case over the phone with someone who is in jail. Jail calls are recorded and we have seen too many cases go south based on remarks made over recorded lines.

Police Reports and Discovery

We will do our best to provide you with copies of everything we receive on your case. Most information will be emailed, so please keep your email address up to date.

Changes in Contact Information

If you move or change numbers during the case, please let us know. It is difficult to help if we are unable to reach you, and helping you is why we are here.

Court Appearances

Cases do not get resolved as quickly as they do on television. Expect there to be several hearings in your case and it may be necessary for you to attend one or more of them. If a hearing is set, you will receive notice of the date and time of each hearing.

Billing and Collections

We understand that this investment was a huge decision for you. As we focus on providing the best representation, we will need for you to stay on schedule with any payment arrangements agreed to at the time of your initial consultation.

Again, thank you for your trust in us. We look forward to getting a fantastic outcome on your case.

Target Market(s)

Criminal defense clients and their families

Industry/Entity Type

Legal

Font styles to use
Serif

Requirements
Must have
• Must incorporate all of the rules we email out. Would like diagrams, images or pictures
Nice to have
• We attached a Welcome brochure. Not sure I want it to look super similar, hence the request for infographic.

```html
<!DOCTYPE html>
<html lang="en">
<head>
<meta charset="utf-8">
<title>Your Legal Journey Starts Here</title>
<link rel="stylesheet" href="https://fonts.googleapis.com/css2?family=Catamaran:wght@700;800&family=Encode+Sans+Condensed:wght@400;700&family=Noto+Sans:wght@400&family=Montserrat:wght@700&display=swap">
<style>
  :root {
    --panel: #eef0f4;
    --card: #ffffff;
    --ink: #111318;
    --body-ink: #1f2228;
    --blue: #0ba3e3;
    --green: #8cc63f;
    --teal: #1bb59a;
    --grey: #8e8f93;
    --link-blue: #1d5fbf;
  }
  * { box-sizing: border-box; margin: 0; padding: 0; }
  html, body { width: 1200px; height: 675px; overflow: hidden; background: var(--panel); }
  .infographic { position: relative; width: 1200px; height: 675px; background: var(--panel); font-family: "Encode Sans Condensed", "Arial Narrow", sans-serif; color: var(--body-ink); }

  .title { position: absolute; top: 36px; left: 0; width: 100%; text-align: center; font-family: "Catamaran", sans-serif; font-weight: 800; font-size: 29px; color: var(--ink); letter-spacing: 0.2px; }
  .subtitle { position: absolute; top: 83px; left: 0; width: 100%; text-align: center; font-family: "Noto Sans", sans-serif; font-size: 17.5px; color: var(--ink); }

  .rule-card { position: absolute; background: var(--card); border-radius: 6px; box-shadow: 0 3px 8px rgba(0,0,0,0.12); }
  .rule-copy { position: absolute; text-align: center; }
  .rule-heading { font-weight: 700; font-size: 11.5px; line-height: 15px; color: var(--ink); }
  .rule-body { font-size: 9.4px; line-height: 13.4px; margin-top: 12px; }
  .rule-body p + p { margin-top: 13px; }

  .badge { position: absolute; border-radius: 50%; display: flex; align-items: center; justify-content: center; box-shadow: 0 2px 6px rgba(0,0,0,0.18); }
  .badge svg { width: 52%; height: 52%; }
  .badge.blue { background: var(--blue); }
  .badge.green { background: var(--green); }
  .badge.teal { background: var(--teal); }
  .badge.grey { background: var(--grey); }
  .rule-number { flex-direction: column; color: #fff; font-family: "Catamaran", sans-serif; font-weight: 800; font-size: 13px; line-height: 14px; text-align: center; }

  .closing { position: absolute; top: 562px; left: 0; width: 100%; text-align: center; font-family: "Noto Sans", sans-serif; font-size: 11.6px; color: var(--ink); }
  .brand { position: absolute; top: 585px; left: 0; width: 100%; display: flex; justify-content: center; align-items: center; gap: 10px; }
  .brand-mark { width: 20px; height: 20px; background: var(--blue); }
  .brand-name { font-family: "Montserrat", sans-serif; font-weight: 700; font-size: 30px; color: var(--ink); letter-spacing: 0.5px; }
  .brand-url { position: absolute; top: 626px; left: 0; width: 100%; text-align: center; font-family: "Noto Sans", sans-serif; font-size: 10px; letter-spacing: 9px; color: var(--link-blue); }
</style>
</head>
<body>
<main class="infographic">
  <h1 class="title">Your Legal Journey Starts Here</h1>
  <p class="subtitle">We're here to help you through every step. Here's what you need to know as a new client.</p>

  <!-- Rule 01 -->
  <section class="rule-card" style="left:52px;top:156px;width:149px;height:374px;"></section>
  <div class="rule-copy" style="left:58px;top:209px;width:137px;">
    <h2 class="rule-heading">Communications</h2>
    <div class="rule-body" style="margin-top:25px;"><p>As a client, you should always be in the loop. While we will try to respond to questions as quickly as possible, sometimes we are unable to respond right away. Do not worry - we promise to get back to you soon. Some questions might take some time to research, and a correct answer is better than a quick one.</p></div>
  </div>
  <div class="badge blue" style="left:86px;top:108px;width:80px;height:80px;">
    <svg viewBox="0 0 40 40"><rect x="4" y="9" width="32" height="22" rx="2" fill="#fff"/><path d="M5 10 L20 22 L35 10 M5 30 L16 19 M35 30 L24 19" stroke="#0ba3e3" stroke-width="2.2" fill="none"/></svg>
  </div>
  <div class="badge blue rule-number" style="left:86px;top:496px;width:80px;height:80px;"><span>RULE</span><span>01</span></div>

  <!-- Rule 02 -->
  <section class="rule-card" style="left:221px;top:161px;width:139px;height:359px;"></section>
  <div class="rule-copy" style="left:226px;top:209px;width:129px;">
    <h2 class="rule-heading">Appointments</h2>
    <div class="rule-body" style="margin-top:15px;"><p>One of the benefits of having an attorney is the ability to discuss your case outside of court, minus the stress and headaches. If you need an appointment, please contact the office.</p><p>Appointments must be scheduled in advance. We do not want you to make a special trip to the office only to learn that we are in court or otherwise unavailable.</p></div>
  </div>
  <div class="badge green" style="left:251px;top:119px;width:76px;height:76px;">
    <svg viewBox="0 0 40 40"><rect x="4" y="7" width="26" height="24" rx="2" fill="none" stroke="#fff" stroke-width="2.2"/><line x1="4" y1="13" x2="30" y2="13" stroke="#fff" stroke-width="2.2"/><line x1="10" y1="4" x2="10" y2="9" stroke="#fff" stroke-width="2.2"/><line x1="24" y1="4" x2="24" y2="9" stroke="#fff" stroke-width="2.2"/><g fill="#fff"><rect x="8" y="17" width="3" height="3"/><rect x="13" y="17" width="3" height="3"/><rect x="18" y="17" width="3" height="3"/><rect x="8" y="23" width="3" height="3"/><rect x="13" y="23" width="3" height="3"/></g><circle cx="28" cy="28" r="8" fill="#8cc63f" stroke="#fff" stroke-width="2.2"/><path d="M24 28 L27 31 L33 24" stroke="#fff" stroke-width="2.4" fill="none"/></svg>
  </div>
  <div class="badge green rule-number" style="left:251px;top:487px;width:76px;height:76px;"><span>RULE</span><span>02</span></div>

  <!-- Rule 03 -->
  <section class="rule-card" style="left:374px;top:181px;width:139px;height:318px;"></section>
  <div class="rule-copy" style="left:378px;top:215px;width:131px;">
    <h2 class="rule-heading">Jail Visits</h2>
    <div class="rule-body" style="margin-top:5px;"><p>If your family member is currently in jail, we take that very seriously. We will visit your loved one and introduce ourselves. While the case is ongoing, we ask that a family member be designated a “contact” person so that messages can be relayed quickly. Never discuss the facts of the case over the phone with someone who is in jail. Jail calls are recorded and we have seen too many cases go south based on remarks made over recorded lines.</p></div>
  </div>
  <div class="badge blue" style="left:405px;top:138px;width:76px;height:76px;">
    <svg viewBox="0 0 40 40"><rect x="5" y="4" width="30" height="32" fill="none" stroke="#fff" stroke-width="2"/><g stroke="#fff" stroke-width="1.8"><line x1="11" y1="4" x2="11" y2="36"/><line x1="17" y1="4" x2="17" y2="36"/><line x1="23" y1="4" x2="23" y2="36"/><line x1="29" y1="4" x2="29" y2="36"/><line x1="5" y1="10" x2="35" y2="10"/></g></svg>
  </div>
  <div class="badge blue rule-number" style="left:405px;top:468px;width:76px;height:76px;"><span>RULE</span><span>03</span></div>

  <!-- Rule 04 -->
  <section class="rule-card" style="left:528px;top:200px;width:139px;height:279px;"></section>
  <div class="rule-copy" style="left:533px;top:249px;width:129px;">
    <h2 class="rule-heading">Police Reports and Discovery</h2>
    <div class="rule-body" style="margin-top:14px;"><p>We will do our best to provide you with copies of everything we receive on your case. Most information will be emailed, so please keep your email address up to date.</p></div>
  </div>
  <div class="badge teal" style="left:560px;top:157px;width:76px;height:76px;">
    <svg viewBox="0 0 40 40"><rect x="8" y="7" width="20" height="26" fill="none" stroke="#fff" stroke-width="2"/><rect x="12" y="4" width="20" height="26" fill="#1bb59a" stroke="#fff" stroke-width="2"/><g stroke="#fff" stroke-width="1.8"><line x1="16" y1="11" x2="28" y2="11"/><line x1="16" y1="15" x2="28" y2="15"/><line x1="16" y1="19" x2="28" y2="19"/><line x1="16" y1="23" x2="24" y2="23"/></g></svg>
  </div>
  <div class="badge teal rule-number" style="left:560px;top:449px;width:76px;height:76px;"><span>RULE</span><span>04</span></div>

  <!-- Rule 05 -->
  <section class="rule-card" style="left:681px;top:178px;width:140px;height:324px;"></section>
  <div class="rule-copy" style="left:686px;top:247px;width:130px;">
    <h2 class="rule-heading">Changes in Contact Information</h2>
    <div class="rule-body" style="margin-top:16px;"><p>If you move or change numbers during the case, please let us know. It is difficult to help if we are unable to reach you, and helping you is why we are here.</p></div>
  </div>
  <div class="badge grey" style="left:713px;top:135px;width:76px;height:76px;">
    <svg viewBox="0 0 40 40"><path d="M20 6 C13 6 11 12 11 18 L11 25 L8 29 L32 29 L29 25 L29 18 C29 12 27 6 20 6 Z" fill="#fff"/><circle cx="20" cy="32" r="3" fill="#fff"/><path d="M6 14 C6 10 8 7 10 5 M34 14 C34 10 32 7 30 5" stroke="#fff" stroke-width="2" fill="none"/></svg>
  </div>
  <div class="badge grey rule-number" style="left:713px;top:466px;width:76px;height:76px;"><span>RULE</span><span>05</span></div>

  <!-- Rule 06 -->
  <section class="rule-card" style="left:836px;top:160px;width:139px;height:359px;"></section>
  <div class="rule-copy" style="left:840px;top:218px;width:131px;">
    <h2 class="rule-heading">Court Appearances</h2>
    <div class="rule-body" style="margin-top:26px;"><p>Cases do not get resolved as quickly as they do on television. Expect there to be several hearings in your case and it may be necessary for you to attend one or more of them. If a hearing is set, you will receive notice of the date and time of each hearing.</p></div>
  </div>
  <div class="badge blue" style="left:867px;top:117px;width:76px;height:76px;">
    <svg viewBox="0 0 40 40"><circle cx="20" cy="20" r="17" fill="#0ba3e3" stroke="#111" stroke-width="3"/><circle cx="20" cy="20" r="14" fill="none" stroke="#fff" stroke-width="1" stroke-dasharray="1 2.6"/><path d="M20 20 L20 10 M20 20 L27 23" stroke="#111" stroke-width="2"/><circle cx="20" cy="20" r="1.6" fill="#111"/></svg>
  </div>
  <div class="badge blue rule-number" style="left:868px;top:484px;width:76px;height:76px;"><span>RULE</span><span>06</span></div>

  <!-- Rule 07 -->
  <section class="rule-card" style="left:999px;top:152px;width:150px;height:376px;"></section>
  <div class="rule-copy" style="left:1005px;top:203px;width:138px;">
    <h2 class="rule-heading">Billing and Collections</h2>
    <div class="rule-body" style="margin-top:27px;"><p>We understand that this investment was a huge decision for you. As we focus on providing the best representation, we will need for you to stay on schedule with any payment arrangements agreed to at the time of your initial consultation.</p></div>
  </div>
  <div class="badge grey" style="left:1034px;top:104px;width:80px;height:80px;">
    <svg viewBox="0 0 40 40"><rect x="3" y="10" width="32" height="18" fill="none" stroke="#fff" stroke-width="1.8" transform="rotate(-6 20 20)"/><rect x="4" y="12" width="32" height="18" fill="#8e8f93" stroke="#fff" stroke-width="2"/><circle cx="20" cy="21" r="5" fill="none" stroke="#fff" stroke-width="1.8"/><text x="20" y="24" text-anchor="middle" font-size="8" font-weight="700" fill="#fff" font-family="Arial, sans-serif">$</text></svg>
  </div>
  <div class="badge grey rule-number" style="left:1034px;top:493px;width:80px;height:80px;"><span>RULE</span><span>07</span></div>

  <p class="closing">Again, thank you for your trust in us. We look forward to getting a fantastic outcome on your case.</p>
  <div class="brand"><span class="brand-mark"></span><span class="brand-name">HARBOR DEFENSE PARTNERS</span></div>
  <p class="brand-url">WWW.HARBORDEFENSEPARTNERS.COM</p>
</main>
</body>
</html>
```